Hello There
i have done the design with one of the pixel harbor designers, now i would like to do the app design as well as the website, business cards, flyers, etc..
the product is an app to help people find anything anywehere and a ale to make time for more important things.
thanks for your support
milo
Updates

Hello ThereI think you got me wrongthe app is not for MORVEX, it is for LumoraUAE.Morvex was just a featured company as an example.how do i send you the Lumorauae logo to base you designs on?it is an application to help people find anything anywhere and make time from more important thingsit has been a few days waiting for this, so it is urgent now.thanksRudy Added Wednesday, August 17, 2016

Target Market(s)

United Arab Emirates

Industry/Entity Type

Business

Contact Information for Business Card

logo, tag line, name title , english and arabic

Number of Pages Required

5+ page

Font styles to use
Sans Serif

```html
<!DOCTYPE html>
<html lang="en">
<head>
<meta charset="utf-8">
<title>LumoraUAE – Home Screen</title>
<link href="https://fonts.googleapis.com/css2?family=Roboto:wght@300;400;500;700&display=swap" rel="stylesheet">
<style>
  :root {
    --stage: #200205;
    --status-blue: #0b72a8;
    --header-light: #cdeefa;
    --header-mid: #a9dbef;
    --main-top: #0d6898;
    --main-bottom: #043a5d;
    --tab-dark: #0a5681;
    --tile-white: #ffffff;
    --tile-shade: #e4e9ec;
    --icon-blue: #2f8fc0;
    --brand-blue: #0a68a0;
    --accent-line: #3b9fd0;
    --nav-black: #000000;
    --text-white: #ffffff;
  }
  * { box-sizing: border-box; margin: 0; padding: 0; }
  html, body {
    width: 1200px; height: 944px; overflow: hidden;
    background: var(--stage);
    font-family: "Roboto", sans-serif;
  }
  .canvas { position: relative; width: 1200px; height: 944px; }
  .screen {
    position: absolute; left: 430px; top: 193px;
    width: 360px; height: 640px;
    transform: scale(0.9444); transform-origin: 0 0;
    overflow: hidden;
    background: linear-gradient(180deg, var(--main-top) 0%, var(--main-bottom) 100%);
  }
  .status-bar {
    position: absolute; left: 0; top: 0; width: 360px; height: 25px;
    background: var(--status-blue); color: var(--text-white);
    display: flex; align-items: center; justify-content: flex-end;
    gap: 6px; padding-right: 8px; font-size: 13px; font-weight: 700;
  }
  .header-band {
    position: absolute; left: 0; top: 25px; width: 360px; height: 78px;
    background: linear-gradient(90deg, var(--header-mid), var(--header-light) 40%, var(--header-light) 70%, var(--header-mid));
  }
  .lang-tab {
    position: absolute; top: 25px; height: 24px; width: 40px;
    background: var(--tab-dark); color: var(--text-white);
    border-radius: 0 0 5px 5px; font-size: 10px; font-weight: 700;
    display: flex; align-items: center; justify-content: center;
  }
  .lang-en { left: 265px; }
  .lang-ara { left: 308px; }
  .brand-holder {
    position: absolute; left: 138px; top: 45px; width: 81px; height: 79px;
    background: var(--header-light); border-radius: 12px;
  }
  .brand-tile {
    position: absolute; left: 7px; top: 4px; width: 67px; height: 67px;
    background: var(--tab-dark); border-radius: 10px;
    display: flex; align-items: center; justify-content: center;
    color: var(--text-white); font-size: 11px; font-weight: 700;
  }
  .headline {
    position: absolute; left: 0; top: 144px; width: 360px; text-align: center;
    color: var(--text-white); font-size: 22px; font-weight: 400;
  }
  .menu-tile {
    position: absolute; width: 86px; height: 60px; border-radius: 10px;
    background: linear-gradient(180deg, var(--tile-white) 60%, var(--tile-shade));
    box-shadow: 0 2px 4px rgba(0,0,0,0.25);
    display: flex; align-items: center; justify-content: center;
  }
  .menu-label {
    position: absolute; width: 120px; text-align: center;
    color: var(--text-white); font-size: 14px; font-weight: 300;
  }
  .ads-box {
    position: absolute; left: 28px; top: 448px; width: 306px; height: 126px;
    border-radius: 10px; background: linear-gradient(180deg, var(--tile-shade) 0, var(--tile-white) 10%, var(--tile-white) 85%, var(--tile-shade));
    color: var(--brand-blue); text-align: center;
  }
  .ads-title { font-size: 62px; font-weight: 400; line-height: 1; margin-top: 22px; }
  .ads-sub { font-size: 28px; font-weight: 400; line-height: 1; margin-top: -2px; }
  .accent-line { position: absolute; left: 0; top: 589px; width: 360px; height: 4px; background: var(--accent-line); }
  .nav-bar {
    position: absolute; left: 0; top: 593px; width: 360px; height: 47px;
    background: var(--nav-black);
  }
</style>
</head>
<body>
<div class="canvas">
  <div class="screen">
    <div class="status-bar">
      <svg width="16" height="14" viewBox="0 0 16 14"><circle cx="8" cy="8" r="5" fill="none" stroke="#fff" stroke-width="1.8"/><path d="M8 5v3l2 1" stroke="#fff" stroke-width="1.5" fill="none"/><path d="M2 3l3-2M14 3l-3-2" stroke="#fff" stroke-width="1.5"/></svg>
      <svg width="18" height="13" viewBox="0 0 18 13"><path d="M0 2 Q9 -3 18 2 L9 13Z" fill="#fff"/></svg>
      <svg width="14" height="13" viewBox="0 0 14 13"><path d="M0 13 L14 0 V13Z" fill="#fff"/></svg>
      <svg width="8" height="14" viewBox="0 0 8 14"><rect x="0" y="2" width="8" height="12" rx="1" fill="#fff"/><rect x="2" y="0" width="4" height="2" fill="#fff"/></svg>
      <span class="clock">16:54</span>
    </div>

    <div class="header-band" role="img" aria-label="Soft blurred light blue header backdrop"></div>
    <div class="lang-tab lang-en">EN</div>
    <div class="lang-tab lang-ara">ARA</div>

    <div class="brand-holder">
      <div class="brand-tile">LumoraUAE</div>
    </div>

    <h1 class="headline">What are you looking for?</h1>

    <div class="menu-tile" style="left:28px; top:190px;">
      <svg width="36" height="36" viewBox="0 0 36 36"><circle cx="15" cy="15" r="11" fill="none" stroke="var(--icon-blue)" stroke-width="4"/><path d="M23 23l9 9" stroke="var(--icon-blue)" stroke-width="5" stroke-linecap="round"/><path d="M11 16l5-6h4v4l-5 6z" fill="var(--icon-blue)"/></svg>
    </div>
    <div class="menu-label" style="left:11px; top:256px;">NAME</div>

    <div class="menu-tile" style="left:138px; top:190px;">
      <svg width="54" height="46" viewBox="0 0 54 46"><rect x="2" y="8" width="22" height="10" rx="3" fill="var(--icon-blue)"/><path d="M6 8l3-6h8l3 6z" fill="var(--icon-blue)"/><circle cx="38" cy="10" r="7" fill="none" stroke="var(--icon-blue)" stroke-width="3"/><path d="M43 15l6 6" stroke="var(--icon-blue)" stroke-width="4" stroke-linecap="round"/><path d="M2 28h4l3 10h13l2-8H8" fill="none" stroke="var(--icon-blue)" stroke-width="3"/><circle cx="11" cy="42" r="2" fill="var(--icon-blue)"/><circle cx="20" cy="42" r="2" fill="var(--icon-blue)"/><circle cx="43" cy="30" r="5" fill="var(--icon-blue)"/><path d="M34 44a9 8 0 0 1 18 0z" fill="var(--icon-blue)"/></svg>
    </div>
    <div class="menu-label" style="left:121px; top:256px;">CATEGORY</div>

    <div class="menu-tile" style="left:248px; top:190px;">
      <svg width="26" height="36" viewBox="0 0 26 36"><path d="M13 0a12 12 0 0 1 12 12c0 9-12 24-12 24S1 21 1 12A12 12 0 0 1 13 0z" fill="var(--icon-blue)"/><circle cx="13" cy="12" r="4.5" fill="#fff"/></svg>
    </div>
    <div class="menu-label" style="left:231px; top:256px;">NEAR BY</div>

    <div class="menu-tile" style="left:138px; top:283px;">
      <svg width="40" height="36" viewBox="0 0 40 36" fill="none" stroke="var(--icon-blue)" stroke-width="1.5"><circle cx="8" cy="8" r="4"/><circle cx="32" cy="8" r="4"/><circle cx="20" cy="13" r="5"/><path d="M1 22a7 6 0 0 1 14 0v3H1z"/><path d="M25 22a7 6 0 0 1 14 0v3H25z"/><path d="M10 32a10 9 0 0 1 20 0v3H10z"/></svg>
    </div>
    <div class="menu-label" style="left:121px; top:349px;">UAE JOBS</div>

    <div class="menu-tile" style="left:28px; top:347px;">
      <svg width="38" height="34" viewBox="0 0 38 34"><rect x="2" y="14" width="20" height="15" rx="1" fill="var(--icon-blue)"/><path d="M2 15l10 7 10-7" stroke="#fff" stroke-width="1.5" fill="none"/><path d="M24 2c-2 1-3 4-1 8s5 7 9 8c2 0 3-2 4-3l-4-3-2 2c-2-1-4-3-5-5l2-2-3-5z" fill="var(--icon-blue)"/></svg>
    </div>
    <div class="menu-label" style="left:9px; top:413px;">SUPPORT</div>

    <div class="menu-tile" style="left:248px; top:347px;">
      <svg width="36" height="36" viewBox="0 0 36 36"><circle cx="15" cy="15" r="11" fill="none" stroke="var(--icon-blue)" stroke-width="4"/><path d="M23 23l9 9" stroke="var(--icon-blue)" stroke-width="5" stroke-linecap="round"/><circle cx="12" cy="12" r="2.5" fill="var(--icon-blue)"/><circle cx="18" cy="13" r="2.5" fill="var(--icon-blue)"/><path d="M8 20a4 3 0 0 1 8 0zM14 21a4 3 0 0 1 8 0z" fill="var(--icon-blue)"/></svg>
    </div>
    <div class="menu-label" style="left:229px; top:412px;">ABOUT US</div>

    <div class="ads-box">
      <div class="ads-title">Ads</div>
      <div class="ads-sub">Featured Comp.</div>
    </div>

    <div class="accent-line"></div>
    <nav class="nav-bar">
      <svg width="360" height="47" viewBox="0 0 360 47" fill="none" stroke="#fff" stroke-width="1.6"><path d="M87 15v16l-13-8z"/><circle cx="180" cy="23" r="8"/><rect x="273" y="16" width="14" height="14"/></svg>
    </nav>
  </div>
</div>
</body>
</html>
```